Flyer-Design für Ferienhaus auf Sylt
Zielgruppe
Ferienhaus auf Sylt im ruhigen und traditionellen Ort Archsum. Zielgruppe ruhe- und erholungssuchende Erwachsene, Familien mit Kind und evtl. mit Hund. Ferienhaus 'klein, aber fein' in ruhiger Lager mit großem Grundstück.
Homepage: duenenkate-wiesmoor.de
Aufgabenstellung
Format DIN LANG / 4 Seiten: Es sollen keine Saisonzeiten und auch keine Preise genannt werden. Es soll nur genannt werden, dass das Haus ab 50 EUR / Tag gemietet werden kann. Bitte nicht die vollständige Adresse des Objektes angeben, lediglich „Sylt-Archsum“. Kontakdtaen bitte auf der Rückseite nennen (siehe Homepage). Kontaktaufnahme bevorzugt per Mail / Anfrageformular v. Homepage. Gerne meine Bilder nutzen, bin aber auch offen für 2-3 Bilder aus dem Stock. Kleine Texte formulieren und gerne mehrere Bilder des Hauses zeigen.

```html
<!DOCTYPE html>
<html lang="de">
<head>
<meta charset="utf-8">
<title>Dünenkate Wiesmoor – Flyer DIN lang</title>
<link href="https://fonts.googleapis.com/css2?family=Playfair+Display:wght@400&family=Parisienne&family=Mulish:wght@400;600&display=swap" rel="stylesheet">
<style>
  :root {
    --blue: #4a78a3;
    --paper: #ffffff;
    --paper-grey: #e9eaee;
    --ink: #3a3d42;
    --stage: #e4e5e8;
    --tone-green: #9db98a;
    --tone-green-soft: #b4c9a4;
    --tone-sky: #bcd7e6;
    --tone-sand: #d3ccaa;
  }
  * { box-sizing: border-box; margin: 0; padding: 0; }
  html, body { width: 710px; height: 1200px; overflow: hidden; }
  body {
    background: var(--stage);
    font-family: "Mulish", sans-serif;
    color: var(--ink);
    position: relative;
  }
  .spread {
    position: absolute;
    left: 91px;
    width: 528px;
    height: 560px;
    display: flex;
    box-shadow: 0 6px 18px rgba(0,0,0,0.12);
  }
  .spread--outside { top: 30px; }
  .spread--inside { top: 610px; }
  .panel {
    position: relative;
    width: 264px;
    height: 560px;
    overflow: hidden;
    background: var(--paper);
  }
  .panel + .panel { border-left: 1px solid rgba(0,0,0,0.06); }
  .photo { position: absolute; left: 0; width: 100%; }
  .band {
    position: absolute;
    left: 0;
    width: 100%;
    background: var(--blue);
    color: var(--paper);
    text-align: center;
  }
  .brand {
    font-family: "Playfair Display", serif;
    font-weight: 400;
    letter-spacing: 0.3px;
    white-space: nowrap;
  }
  .brand-dot {
    display: block;
    margin: 0 auto;
    border-radius: 50%;
    background: var(--paper);
  }
  .script {
    font-family: "Parisienne", cursive;
    font-weight: 400;
  }

  /* Back panel */
  .back .photo--house-field {
    top: 0; height: 150px;
    background: linear-gradient(180deg, var(--tone-green-soft), var(--tone-green));
  }
  .back .band { top: 150px; height: 78px; padding-top: 10px; }
  .back .brand-dot { width: 24px; height: 24px; margin-bottom: 4px; }
  .back .brand { font-size: 20px; line-height: 1.1; }
  .back .place { font-size: 9.5px; letter-spacing: 0.5px; opacity: 0.9; margin-top: 3px; }
  .contact {
    position: absolute;
    top: 228px; left: 0; width: 100%; height: 136px;
    background: var(--paper-grey);
    display: flex;
    align-items: center;
    padding: 0 14px 0 22px;
  }
  .contact-label {
    color: var(--blue);
    font-size: 10px;
    line-height: 1.25;
    letter-spacing: 0.4px;
    text-transform: uppercase;
    width: 78px;
  }
  .contact-list {
    list-style: none;
    border-left: 1px solid var(--blue);
    padding: 4px 0 4px 10px;
    font-size: 9.5px;
    line-height: 1.35;
    white-space: nowrap;
  }
  .contact-list .gap { margin-top: 7px; }
  .back .collage { position: absolute; top: 364px; left: 0; width: 264px; height: 196px; }

  /* Front panel */
  .front .photo--house { top: 0; height: 205px;
    background: linear-gradient(180deg, var(--tone-sky), var(--tone-green)); }
  .front .brand-dot { position: absolute; top: 178px; left: 50%; width: 48px; height: 48px; margin-left: -24px; z-index: 2; }
  .front .band { top: 205px; height: 58px; padding-top: 22px; }
  .front .brand { font-size: 24px; }
  .front .photo--dunes { top: 263px; height: 297px;
    background: linear-gradient(180deg, var(--tone-sky), var(--tone-sand)); }
  .front .tagline {
    position: absolute; top: 300px; left: 0; width: 100%;
    text-align: center; color: var(--paper);
    font-size: 27px; line-height: 1.15;
  }

  /* Inside left */
  .inside-left .collage { position: absolute; top: 0; left: 0; width: 264px; height: 300px; }
  .features {
    position: absolute; top: 300px; left: 0; width: 100%; height: 260px;
    padding: 30px 8px 0;
    text-align: center;
  }
  .features h2 { color: var(--blue); font-size: 21px; margin-bottom: 14px; white-space: nowrap; }
  .features ul { list-style: none; font-size: 9px; line-height: 1.85; white-space: nowrap; }

  /* Inside right */
  .intro {
    position: absolute; top: 0; left: 0; width: 100%; height: 252px;
    background: var(--paper-grey);
    padding: 26px 20px 0;
  }
  .intro-head { display: flex; align-items: center; justify-content: center; gap: 6px; margin-bottom: 16px; }
  .intro-head .brand-dot { width: 26px; height: 26px; background: var(--blue); margin: 0; order: 2; }
  .intro-head .brand { color: var(--blue); font-size: 19px; }
  .intro p { font-size: 8.8px; line-height: 1.45; text-align: justify; margin-bottom: 9px; }
  .intro .facts { text-align: left; }
  .inside-right .gallery { position: absolute; top: 252px; left: 0; width: 264px; height: 252px; }
  .inside-right .band { top: 504px; height: 56px; padding-top: 10px; }
  .inside-right .band small { display: block; font-size: 8.5px; letter-spacing: 0.3px; margin-bottom: 3px; }
  .inside-right .band .brand { font-size: 16px; }
</style>
</head>
<body>

<section class="spread spread--outside">
  <article class="panel back">
    <div class="photo photo--house-field" role="img" aria-label="Foto: Ferienhaus hinter Wiese und Büschen"></div>
    <div class="band">
      <span class="brand-dot"></span>
      <div class="brand">Dünenkate Wiesmoor</div>
      <div class="place">Sylt-Archsum</div>
    </div>
    <div class="contact">
      <div class="contact-label">Anfragen &amp;<br>Buchungen</div>
      <ul class="contact-list">
        <li>T: 030 555 014 27</li>
        <li>M: 0170 555 21 09</li>
        <li>F: 030 555 014 28</li>
        <li class="gap">strandkatehuus@post-mail.de</li>
        <li class="gap">duenenkate-wiesmoor.de</li>
      </ul>
    </div>
    <svg class="collage" viewBox="0 0 264 196">
      <polygon role="img" aria-label="Foto: Holzsteg durch die Dünen" points="90,0 264,0 264,60 132,98" fill="#b3c2a0" stroke="#fff" stroke-width="3"/>
      <polygon role="img" aria-label="Foto: Sonnenuntergang über der Heide" points="0,22 90,0 132,98 30,196 0,196" fill="#b99a80" stroke="#fff" stroke-width="3"/>
      <polygon role="img" aria-label="Foto: Strand mit Buhnen und Strandkörben" points="264,60 264,196 190,196 132,98" fill="#a9a8a2" stroke="#fff" stroke-width="3"/>
      <polygon role="img" aria-label="Foto: Dünenweg zum Sandstrand" points="30,196 190,196 132,98" fill="#d9d3c3" stroke="#fff" stroke-width="3"/>
      <circle role="img" aria-label="Foto: Ferienhaus von vorn" cx="132" cy="98" r="48" fill="#a9958a" stroke="#fff" stroke-width="3"/>
    </svg>
  </article>

  <article class="panel front">
    <div class="photo photo--house" role="img" aria-label="Foto: Klinkerhaus mit Rasen"></div>
    <span class="brand-dot"></span>
    <div class="band"><div class="brand">Dünenkate Wiesmoor</div></div>
    <div class="photo photo--dunes" role="img" aria-label="Foto: Dünengras mit Leuchtturm"></div>
    <p class="tagline script">Ankommen und<br>wohlfühlen</p>
  </article>
</section>

<section class="spread spread--inside">
  <article class="panel inside-left">
    <svg class="collage" viewBox="0 0 264 300">
      <polygon role="img" aria-label="Foto: Garten mit Bäumen und Haus" points="110,0 264,0 264,150 180,110" fill="#9fb68c" stroke="#fff" stroke-width="3"/>
      <polygon role="img" aria-label="Foto: Süd-Terrasse mit Gartenmöbeln" points="0,20 110,0 180,110 120,165 0,120" fill="#bdb8b0" stroke="#fff" stroke-width="3"/>
      <polygon role="img" aria-label="Foto: Sekt und Blumen auf dem Terrassentisch" points="180,110 264,150 264,250 190,215" fill="#a9bf9c" stroke="#fff" stroke-width="3"/>
      <polygon role="img" aria-label="Foto: Helle Einbauküche" points="0,120 120,165 80,300 0,300" fill="#e5dfd2" stroke="#fff" stroke-width="3"/>
      <polygon role="img" aria-label="Foto: Essbereich mit Holztisch" points="120,165 180,110 190,215 264,250 264,300 80,300" fill="#bda68e" stroke="#fff" stroke-width="3"/>
    </svg>
    <div class="features">
      <h2 class="script">Ankommen und wohlfühlen</h2>
      <ul>
        <li>Lichtdurchflutetes Wohnzimmer mit ausziehbarer Couch</li>
        <li>Moderne offene Einbauküche</li>
        <li>Badezimmer im Ober- und Erdgeschoss</li>
        <li>Schlafzimmer mit Doppelbett</li>
        <li>Zweites Schlafzimmer/Kinderzimmer</li>
        <li>PKW-Stellplatz</li>
        <li>Kostenfreies WLAN</li>
        <li>Kontaktlose Anreise mit persönlichem Pin-Code</li>
      </ul>
    </div>
  </article>

  <article class="panel inside-right">
    <div class="intro">
      <div class="intro-head">
        <span class="brand-dot"></span>
        <span class="brand">Dünenkate Wiesmoor</span>
      </div>
      <p>Kleines aber feines Ferienhaus im beschaulichen Ort Archsum auf Sylt in ruhiger Lage mit großem Garten.</p>
      <p>Das freistehende, massiv gebaute Einfamilienhaus bietet Ruhe- und Erholungssuchenden mit ca. 86 m² Wohnfläche, der schönen Süd-Terrasse und dem großen Grundstück (1200 m²) die besten Voraussetzungen zum Entspannen, Sonne tanken und um sich einfach nur wohlzufühlen.</p>
      <p class="facts">Ideal für 2-6 Personen<br>Verfügbar bereits ab € 50,- Tagesmiete</p>
    </div>
    <svg class="gallery" viewBox="0 0 264 252">
      <polygon role="img" aria-label="Foto: Wohnzimmer mit Ecksofa" points="0,0 170,0 170,120 0,120" fill="#a3aec2" stroke="#fff" stroke-width="3"/>
      <polygon role="img" aria-label="Foto: Abendlicht über dem Meer" points="170,0 264,0 264,120 170,120" fill="#b3bac0" stroke="#fff" stroke-width="3"/>
      <polygon role="img" aria-label="Foto: Modernes Badezimmer" points="0,120 130,120 130,252 0,252" fill="#d8d5cf" stroke="#fff" stroke-width="3"/>
      <polygon role="img" aria-label="Foto: Schlafzimmer mit Doppelbett" points="130,120 264,120 264,252 130,252" fill="#cdb798" stroke="#fff" stroke-width="3"/>
    </svg>
    <div class="band">
      <small>Alle Details und Buchungsmöglichkeit auf</small>
      <div class="brand">duenenkate-wiesmoor.de</div>
    </div>
  </article>
</section>

</body>
</html>
```